a Sydney based app company needs a product booklet

we need a 8 pager booklet to introduce the key benefit of our app. The content is included in the doc attached. Also can refer to the design style in our website quillora.au. A updated content doc has been uploaded. Please also add to the end cover 'Powered by OFR' with OFR logo which is also attached.

Retail customers

```html
<!DOCTYPE html>
<html lang="en">
<head>
<meta charset="utf-8">
<title>Quillora Product Booklet</title>
<link href="https://fonts.googleapis.com/css2?family=Poppins:wght@400;500;600;700;800&family=Baloo+2:wght@700;800&display=swap" rel="stylesheet">
<style>
:root{
  --blue:#1c4ea3;
  --blue-dark:#123a80;
  --yellow:#f6b31c;
  --yellow-soft:#fcd56a;
  --white:#ffffff;
  --ink:#1e2a44;
  --muted:#5b6478;
  --canvas:#e6e7eb;
}
*{box-sizing:border-box;margin:0;padding:0}
html,body{width:1200px;height:2972px;overflow:hidden;background:var(--canvas);font-family:"Poppins",Arial,sans-serif;color:var(--ink)}
.booklet{position:relative;width:1200px;height:2972px}
.spread{position:absolute;left:40px;width:1120px;height:700px;display:flex;box-shadow:0 6px 18px rgba(0,0,0,.18)}
.spread-1{top:32px}.spread-2{top:776px}.spread-3{top:1520px}.spread-4{top:2264px}
.page{position:relative;width:560px;height:700px;overflow:hidden;background:var(--white)}
.page+.page{border-left:1px solid rgba(0,0,0,.08)}
.abs{position:absolute}
.photo{position:absolute;border-radius:0}
.photo.round{border-radius:10px}
.heading{font-family:"Baloo 2","Poppins",sans-serif;font-weight:800;line-height:1.05}
.small{font-size:9px;line-height:1.45;color:var(--muted)}
.small.light{color:#dfe6f5}
.tag{display:inline-block;background:var(--yellow);color:var(--blue-dark);font-weight:700;font-size:13px;padding:4px 12px;border-radius:4px}
.tag.blue{background:var(--blue);color:var(--white)}
.brand{font-family:"Poppins",sans-serif;font-weight:700;display:flex;align-items:center;gap:8px}
.brand .dot{width:14px;height:14px;border-radius:50%;background:var(--yellow)}
/* spread 1 */
.back-top{left:0;top:0;width:560px;height:150px;background:var(--blue);padding:22px 28px}
.back-top .heading{color:var(--white);font-size:32px}
.features{display:flex;gap:18px;margin-top:14px}
.feature{flex:1}
.feature b{display:block;font-size:12px;color:var(--yellow);margin-bottom:3px}
.back-bottom{left:0;top:560px;width:560px;height:140px;padding:24px 28px;display:flex;justify-content:space-between}
.back-bottom .heading{color:var(--blue);font-size:22px;width:260px}
.back-bottom .small{width:260px;margin-top:6px}
.contact{text-align:left;font-size:10px;color:var(--blue);line-height:1.8}
.contact .brand{font-size:20px;color:var(--blue);margin-bottom:4px}
.cover-lower{left:0;top:430px;width:560px;height:270px;padding:40px 36px;color:var(--white)}
.cover-lower .brand{font-size:30px;color:var(--white)}
.cover-lower .heading{color:var(--yellow);font-size:32px;margin-top:16px}
.cover-lower .powered{font-size:12px;margin-top:4px}
.call{position:absolute;right:36px;bottom:36px;text-align:right}
.call .heading{font-size:26px;margin:0}
.call .num{font-size:26px;font-weight:800;color:var(--white)}
/* spread 2 */
.welcome{left:30px;bottom:40px;color:var(--blue);font-size:34px}
.intro-box{right:24px;top:28px;width:200px;background:var(--white);padding:12px;border-radius:6px}
.how-top{left:0;top:0;width:560px;height:170px;padding:28px 28px}
.how-top .small{width:270px}
.how-band{left:0;top:170px;width:560px;height:530px;background:var(--blue)}
.how-title{left:28px;top:20px;color:var(--white);font-size:30px}
.step{position:absolute;display:flex;align-items:center;gap:16px}
.step .phone{width:70px;height:110px;border-radius:12px;background:linear-gradient(160deg,#e9eefb,#b9c7e6);border:3px solid var(--white)}
.step h4{font-size:17px;font-weight:700;color:var(--yellow);line-height:1.2}
.step .small{width:200px;margin-top:4px}
.yellow-strip{left:0;bottom:0;width:560px;height:160px;background:var(--yellow)}
/* spread 3 */
.s3-left{background:var(--yellow)}
.s3-left .heading.title{left:28px;top:24px;color:var(--blue);font-size:30px;width:300px}
.five-band{left:0;top:500px;width:560px;height:200px;background:var(--blue);padding:18px 24px}
.five-band h3{color:var(--white);font-size:15px;font-weight:600}
.five-band h3 span{color:var(--yellow);font-size:22px;font-weight:800}
.tiles{display:flex;gap:10px;margin-top:12px}
.tile{flex:1;text-align:center;color:var(--white);font-size:11px;font-weight:600}
.tile .photo{position:static;height:90px;border-radius:6px;margin-bottom:6px}
.svc{position:absolute;width:250px}
.svc h3{font-family:"Baloo 2",sans-serif;font-weight:800;font-size:30px;color:var(--blue);line-height:1}
.svc ul{list-style:none;margin-top:6px}
.svc li{font-size:9px;color:var(--muted);display:flex;align-items:center;gap:5px;margin-bottom:3px}
.svc li::before{content:"";width:6px;height:6px;border-radius:50%;background:var(--yellow)}
.quality{left:0;top:440px;width:560px;height:260px;background:var(--blue);padding:22px 28px}
.quality h3{color:var(--yellow);font-size:18px;font-weight:700}
.quality .tag{margin:12px 0 6px;font-size:11px}
/* spread 4 */
.cost{left:28px;top:28px;width:500px}
.cost .heading{color:var(--blue);font-size:30px}
.cost .tag{margin:12px 0 6px}
.balance{left:0;top:360px;width:560px;height:340px;background:var(--yellow);padding:26px 30px}
.balance .heading{color:var(--blue);font-size:28px;width:330px}
.balance .small{color:var(--ink);margin-top:8px;width:460px}
.opt{display:flex;align-items:flex-start;gap:10px;margin-top:12px}
.opt .ico{flex:none;width:22px;height:22px;border-radius:4px;background:var(--blue)}
.opt b{font-size:12px;color:var(--blue)}
.opt .small{margin-top:2px;width:430px}
</style>
</head>
<body>
<div class="booklet">

<!-- Spread 1: back and front covers -->
<section class="spread spread-1">
  <div class="page back-cover">
    <div class="abs back-top">
      <h2 class="heading">Home Comforts, Effortless</h2>
      <div class="features">
        <div class="feature"><b>Convenient</b><p class="small light">Book trusted help in a few taps from home.</p></div>
        <div class="feature"><b>Affordable</b><p class="small light">Clear pricing with no hidden extras at all.</p></div>
        <div class="feature"><b>Reliable</b><p class="small light">Vetted pros who arrive on time, every time.</p></div>
      </div>
    </div>
    <div class="photo" style="left:0;top:150px;width:560px;height:410px;background:linear-gradient(135deg,#d8dde6,#b7c0cf)" role="img" aria-label="Smiling family standing together in a bright living room"></div>
    <svg class="abs" style="left:0;top:150px" width="560" height="410" viewBox="0 0 560 410">
      <polygon points="420,0 560,0 560,410 470,410" fill="#1c4ea3"/>
      <polygon points="395,0 430,0 485,410 450,410" fill="#f6b31c"/>
    </svg>
    <div class="abs back-bottom">
      <div>
        <h3 class="heading">Ready to experience the convenience at Quillora?</h3>
        <p class="small">Reach out to your trusted home team for regular, seasonal or one-off services today.</p>
      </div>
      <div class="contact">
        <div class="brand"><span class="dot"></span>Quillora</div>
        <div>1300 555 014</div>
        <div>hello@quillora.au</div>
        <div>quillora.au</div>
      </div>
    </div>
  </div>
  <div class="page front-cover">
    <div class="photo" style="left:0;top:0;width:560px;height:440px;background:linear-gradient(160deg,#eef0f3,#c9ced8)" role="img" aria-label="Cleaner wiping a table in a bright modern home"></div>
    <svg class="abs" style="left:0;top:380px" width="560" height="80" viewBox="0 0 560 80">
      <polygon points="0,40 560,0 560,50 0,80" fill="#f6b31c"/>
    </svg>
    <div class="abs cover-lower" style="background:var(--blue);top:440px;height:260px;padding-top:24px">
      <div class="brand"><span class="dot"></span>Quillora</div>
      <h1 class="heading" style="color:var(--yellow);font-size:32px;margin-top:14px">Innovative Home Services</h1>
      <p class="powered">Powered by OFR Smart Home Technology</p>
      <div class="call">
        <p class="heading" style="color:var(--yellow)">Call Us Today</p>
        <p class="num">1300 555 014</p>
      </div>
    </div>
  </div>
</section>

<!-- Spread 2: welcome and how it works -->
<section class="spread spread-2">
  <div class="page">
    <div class="photo" style="left:0;top:0;width:560px;height:700px;background:linear-gradient(150deg,#f1f1ef,#cfd2d6)" role="img" aria-label="Man in an apron cleaning a kitchen bench"></div>
    <div class="abs intro-box"><p class="small">Quillora brings cleaning, car wash, massage and babysitting together in one simple app built for busy homes.</p></div>
    <h2 class="abs heading welcome">Welcome to Quillora.</h2>
  </div>
  <div class="page">
    <div class="abs how-top">
      <p class="small">Discover the benefits of choosing Quillora for your home service needs. Our platform is designed to enhance your lifestyle through convenience and innovation.</p>
    </div>
    <div class="photo" style="left:320px;top:18px;width:220px;height:180px;background:linear-gradient(135deg,#d5dae3,#aab4c6)" role="img" aria-label="Smiling older couple at home"></div>
    <div class="abs how-band">
      <h2 class="abs heading how-title">How it works<br><span style="font-size:12px;font-family:Poppins,sans-serif;font-weight:500">Tap to book. Get Offers. Sit &amp; relax.</span></h2>
      <div class="step" style="left:300px;top:40px;flex-direction:row-reverse">
        <div class="phone"></div>
        <div style="width:150px"><h4>Select the service you need</h4><p class="small light" style="width:150px">Pick from cleaning, car wash and more.</p></div>
      </div>
      <div class="step" style="left:28px;top:170px">
        <div class="phone"></div>
        <div><h4>Choose time and date</h4><p class="small light">Select a slot that suits your week and get instant confirmation.</p></div>
      </div>
      <div class="step" style="left:28px;top:310px">
        <div class="phone"></div>
        <div><h4>Confirm your access preference</h4><p class="small light">Let us in with a temporary code, or be at home when we arrive.</p></div>
      </div>
    </div>
    <div class="abs yellow-strip" style="height:60px"></div>
  </div>
</section>

<!-- Spread 3: booking and services -->
<section class="spread spread-3">
  <div class="page s3-left">
    <h2 class="abs heading title">Streamlined Booking Process</h2>
    <p class="abs small" style="left:28px;top:100px;width:300px;color:var(--ink)">Quillora makes scheduling simple: browse services, pick a time and manage every booking from one place.</p>
    <span class="abs tag blue" style="left:28px;top:150px">Flexible Booking</span>
    <p class="abs small" style="left:28px;top:185px;width:230px;color:var(--ink)">Book once, weekly or fortnightly and change plans any time without fees.</p>
    <div class="photo round" style="left:290px;top:150px;width:240px;height:130px;background:linear-gradient(135deg,#f3e2b6,#d8b46a)" role="img" aria-label="Woman booking a service on her phone"></div>
    <div class="photo round" style="left:28px;top:310px;width:240px;height:130px;background:linear-gradient(135deg,#f5e7c0,#d9b86c)" role="img" aria-label="Person checking a schedule on a tablet"></div>
    <span class="abs tag blue" style="left:290px;top:310px">Real-Time Scheduling</span>
    <p class="abs small" style="left:290px;top:345px;width:240px;color:var(--ink)">See live availability and get notified the moment your pro is on the way.</p>
    <div class="abs five-band">
      <h3>Get your home organised in <span>5 clicks</span></h3>
      <div class="tiles">
        <div class="tile"><div class="photo" style="background:linear-gradient(135deg,#cfd6e4,#9eabc3)" role="img" aria-label="Home cleaning"></div>Cleaning</div>
        <div class="tile"><div class="photo" style="background:linear-gradient(135deg,#cfd6e4,#9eabc3)" role="img" aria-label="Car being washed"></div>Car Wash</div>
        <div class="tile"><div class="photo" style="background:linear-gradient(135deg,#cfd6e4,#9eabc3)" role="img" aria-label="Massage session"></div>Massage</div>
        <div class="tile"><div class="photo" style="background:linear-gradient(135deg,#cfd6e4,#9eabc3)" role="img" aria-label="Babysitter with child"></div>Babysitting</div>
        <div class="tile"><div class="photo" style="background:linear-gradient(135deg,#cfd6e4,#9eabc3)" role="img" aria-label="Pet care"></div>Pet Care</div>
      </div>
    </div>
  </div>
  <div class="page">
    <div class="photo round" style="left:24px;top:22px;width:120px;height:90px;background:linear-gradient(135deg,#e8e2d6,#c7baa0)" role="img" aria-label="Cleaner dusting shelves"></div>
    <div class="photo round" style="left:152px;top:22px;width:120px;height:90px;background:linear-gradient(135deg,#dde3ec,#a8b5c8)" role="img" aria-label="Car being washed"></div>
    <div class="photo round" style="left:288px;top:22px;width:120px;height:90px;background:linear-gradient(135deg,#ecdcd0,#c9a993)" role="img" aria-label="Massage therapy"></div>
    <div class="photo round" style="left:416px;top:22px;width:120px;height:90px;background:linear-gradient(135deg,#e4e0ea,#b6abc8)" role="img" aria-label="Babysitter reading with child"></div>
    <div class="svc" style="left:24px;top:124px"><h3>Cleaning</h3><ul><li>Regular Clean</li><li>Deep Clean</li><li>End of Lease</li></ul></div>
    <div class="svc" style="left:160px;top:124px"><h3>Car Wash</h3><ul><li>Exterior Wash</li><li>Interior Detail</li><li>Full Valet</li></ul></div>
    <div class="svc" style="left:300px;top:124px"><h3>Massage</h3><ul><li>Relaxation Massage</li><li>Deep Tissue</li><li>Sports Massage</li></ul></div>
    <div class="svc" style="left:300px;top:240px"><h3>Babysitting</h3><p class="small" style="margin-top:6px">Caring, checked sitters for date nights, workdays and school holidays.</p></div>
    <div class="photo round" style="left:24px;top:240px;width:250px;height:180px;background:linear-gradient(135deg,#dde4ee,#aab7cc)" role="img" aria-label="Friendly service professional at work"></div>
    <div class="abs quality">
      <h3>Quality &amp; Consistent Services</h3>
      <p class="small light" style="margin-top:6px">Every Quillora professional follows the same standard so each visit feels just as good as the last.</p>
      <span class="tag">Background Checks</span>
      <p class="small light">All workers pass police and reference checks before their first booking.</p>
      <span class="tag">Standards</span>
      <p class="small light">Clear checklists and customer ratings keep our service quality high.</p>
    </div>
  </div>
</section>

<!-- Spread 4: cost and security -->
<section class="spread spread-4">
  <div class="page">
    <div class="abs cost">
      <h2 class="heading">Cost-Effective Solutions</h2>
      <p class="small" style="margin-top:8px">Our pricing stays fair because we work smarter, matching jobs and routes so savings pass on to you.</p>
      <span class="tag">Economies of Scale</span>
      <p class="small">With many households using one network, we secure better rates on supplies and staffing for every customer.</p>
      <span class="tag">Efficient Job Scheduling</span>
      <p class="small">Smart planning groups nearby bookings, cutting travel time and keeping your service price low.</p>
    </div>
    <div class="photo" style="left:0;top:330px;width:560px;height:370px;background:linear-gradient(150deg,#e5e1dc,#bdb3a8)" role="img" aria-label="Couple saving coins in a piggy bank"></div>
  </div>
  <div class="page">
    <div class="photo" style="left:0;top:0;width:560px;height:360px;background:linear-gradient(160deg,#e2e6ec,#b2bccb)" role="img" aria-label="Cleaner with supplies greeted at a front door"></div>
    <div class="abs balance">
      <h2 class="heading">Perfect Balance of Security and Convenience:</h2>
      <p class="small">Choose how our team enters your home so every visit fits your comfort level.</p>
      <div class="opt"><span class="ico"></span><div><b>Access Granted (via Temporary Passcode)</b><p class="small">A one-time code lets your pro in and expires after the job.</p></div></div>
      <div class="opt"><span class="ico"></span><div><b>Tracking Only:</b><p class="small">Follow arrival and finish times live while you stay at home.</p></div></div>
      <div class="opt"><span class="ico"></span><div><b>Do Not Disturb:</b><p class="small">Your pro works quietly around you with no calls or knocks.</p></div></div>
    </div>
  </div>
</section>

</div>
</body>
</html>
```